New therapy private practice needs a 2 sided postcard announcing location and services

We need a postcard sized card that is TWO SIDED and shares our new location and services offered. (new location is 3840. W. 58th #2200 in Tulsa, OK 74129) Name of the therapy business is "Calm Harbor Counseling". Services offered include individual, marriage, family and group counseling. My phone number to place on the card is (918) 555-0148 and someone can call to schedule a free 20 minute consultation at that number.

These cards will also be mailed in an enclosed envelope or placed in welcome baskets as a marketing tool with possible referral sources like churches, doctors, and lawyers. (That means there does not have to be a space for an address or stamp to mail to. Full use of both sides of the card is important) We would like to see designs that use softer colors such as blue, purples, or greens. The final design should communicate a feeling of peace and hope and a sense of freshness and approachability. Incorporating a tag line such as..... "where you'll find hope!" would be good. My website is www.calmharborcare.example and extra info about my practice is on there. It is important my credentials are listed on the postcard. Dana Ruth Pell, LPC-S, LMFT

I am not looking for a bunch of "box looking pictures". The pictures I am uploading are for ideas, although my logo and picture should be used. I like the type of picture I have on my homepage of my website with the quote "Let your hopes, not your fears shape your future"

Target Market(s)

Primarily women and couples looking for counseling for relationships, anxiety, depression, or life transitions.

Font styles to use
Serif
Script

Colors
3276b5
85acd3
86cfc6
33b8a4
cadf82
876aae
9bcb3c

Requirements
Must have
• My picture, address, website, and phone number as well as my logo.
• Address is: 3840 W. 58th Street #2200 Tulsa, OK 74129
• Web: www.calmharborcare.example
• Email: dana@calmharborcare.example
• Phone: (918) 555-0148
• "Hope anchors the soul" - Heb. 6:19
• On my website, I have a 2 minute video of myself. This may be helpful to watch in getting a "feel" for my counseling practice.
• Services Provided: ANXIETY | DEPRESSION | LIFE TRANSITIONS | MARRIAGE COUNSELING | SEPARATION AND DIVORCE | WOMEN’S ISSUES | ADDICTIONS AND INFIDELITY | PARENT/CHILD RELATIONSHIPS | FAMILY CONFLICT | TRAUMA/GRIEF AND LOSS
Nice to have
• A combination of print and script would be nice. A feeling of tranquility and hope
• I would like to have the statement at the bottom of the card.... " It is my desire for you to discover that no matter the situation you are currently going through….. there’s hope!"
• It would also be nice to have a small area that says: Dana is a graduate of Western Lakeview College and has been in private practice for 11 years. She is a regular monthly co-host on the Meadow Broadcast Group at 88.3 FM
Should not have
• Heavy bold or abrasive feel

```html
<!DOCTYPE html>
<html lang="en">
<head>
<meta charset="utf-8">
<title>Calm Harbor Counseling – Postcard</title>
<link rel="stylesheet" href="https://fonts.googleapis.com/css2?family=Lato:wght@400;700;900&display=swap">
<style>
  :root {
    --stage: #2b2b2b;
    --card-light: #f4f9f9;
    --card-tint: #e3eff1;
    --leaf-green: #4a8a3a;
    --band-green: #4d8a3d;
    --ink: #111111;
    --white: #ffffff;
    --photo-warm: #d9a23a;
    --photo-soft: #b9c6b4;
  }
  * { margin: 0; padding: 0; box-sizing: border-box; }
  html, body { width: 1200px; height: 462px; overflow: hidden; }
  body {
    background: var(--stage);
    font-family: "Lato", Arial, sans-serif;
    position: relative;
  }
  .postcard {
    position: absolute;
    top: 48px;
    width: 550px;
    height: 366px;
    overflow: hidden;
    background: linear-gradient(135deg, var(--card-light) 0%, var(--card-tint) 100%);
  }
  .postcard--front { left: 36px; }
  .postcard--back { left: 614px; }

  .portrait { position: absolute; left: 0; top: 0; }

  .radio-note {
    position: absolute;
    left: 18px;
    top: 226px;
    width: 188px;
    color: var(--white);
    font-size: 9.5px;
    line-height: 1.3;
    text-align: center;
  }

  .brand {
    position: absolute;
    top: 60px;
    display: flex;
    align-items: center;
    gap: 12px;
  }
  .postcard--front .brand { left: 308px; }
  .postcard--back .brand { left: 290px; }
  .brand-dot {
    width: 46px; height: 46px;
    border-radius: 50%;
    background: var(--leaf-green);
    flex: none;
  }
  .brand-name {
    color: var(--leaf-green);
    font-weight: 700;
    font-size: 26px;
    line-height: 1.05;
  }

  .cta {
    position: absolute;
    top: 178px;
    width: 250px;
    text-align: center;
    font-weight: 900;
    font-size: 23.5px;
    line-height: 1.32;
    color: var(--ink);
    letter-spacing: -0.2px;
  }
  .postcard--front .cta { left: 288px; }
  .postcard--back .cta { left: 280px; }
  .cta-highlight { color: var(--leaf-green); display: block; }

  .services {
    position: absolute;
    left: 29px;
    top: 38px;
  }
  .services-title {
    font-weight: 900;
    font-size: 17px;
    color: var(--ink);
    margin-bottom: 7px;
  }
  .services-list { list-style: none; }
  .services-list li {
    display: flex;
    align-items: center;
    gap: 8px;
    color: var(--leaf-green);
    font-weight: 900;
    font-size: 13.2px;
    line-height: 20.4px;
    text-transform: uppercase;
  }
  .services-list svg { flex: none; }

  .contact-band { position: absolute; left: 0; bottom: 0; width: 550px; height: 76px; }
  .contact-text {
    position: absolute;
    left: 0; bottom: 0;
    width: 550px;
    height: 62px;
    text-align: center;
    color: var(--white);
  }
  .contact-address { font-weight: 700; font-size: 14px; line-height: 18px; }
  .contact-lines { font-weight: 700; font-size: 13.4px; line-height: 18px; }
  .contact-promise { font-weight: 700; font-size: 8.4px; line-height: 18px; }
</style>
</head>
<body>

<section class="postcard postcard--front">
  <svg class="portrait" width="300" height="290" viewBox="0 0 300 290">
    <defs>
      <clipPath id="portrait-clip"><circle cx="138" cy="136" r="138"/></clipPath>
      <linearGradient id="portrait-tone" x1="0" y1="0" x2="1" y2="1">
        <stop offset="0" stop-color="var(--photo-warm)"/>
        <stop offset="0.55" stop-color="#c9a47c"/>
        <stop offset="1" stop-color="var(--photo-soft)"/>
      </linearGradient>
    </defs>
    <g clip-path="url(#portrait-clip)">
      <rect role="img" aria-label="Portrait photo of Dana, the counselor, outdoors with autumn leaves behind her" x="-30" y="-20" width="330" height="310" fill="url(#portrait-tone)"/>
      <rect x="-30" y="217" width="330" height="70" fill="#111"/>
    </g>
    <circle cx="138" cy="136" r="138" fill="none" stroke="var(--leaf-green)" stroke-width="4"/>
    <circle cx="138" cy="136" r="142" fill="none" stroke="#111" stroke-width="3"/>
  </svg>
  <p class="radio-note">Dana can be heard monthly on the<br>Meadow Broadcast Group<br>at 88.3 FM</p>

  <div class="brand">
    <span class="brand-dot"></span>
    <span class="brand-name">Calm Harbor<br>Counseling</span>
  </div>

  <h2 class="cta">CALL TO SCHEDULE<span class="cta-highlight">A FREE 20 MINUTE</span>CONSULTATION</h2>

  <svg class="contact-band" viewBox="0 0 550 76" preserveAspectRatio="none">
    <path d="M0 14 Q275 -6 550 14 L550 76 L0 76 Z" fill="#111"/>
    <path d="M0 18 Q275 0 550 18 L550 76 L0 76 Z" fill="var(--band-green)"/>
  </svg>
  <div class="contact-text">
    <p class="contact-address">3840 W. 58th Street #2200 Tulsa, OK 74129</p>
    <p class="contact-lines">www.calmharborcare.example | dana@calmharborcare.example | (918) 555-0148</p>
    <p class="contact-promise">It is my desire for you to discover that no matter the situation you are currently going through….. there’s calm ahead!</p>
  </div>
</section>

<section class="postcard postcard--back">
  <div class="services">
    <h3 class="services-title">ISSUES SERVED:</h3>
    <ul class="services-list">
      <li><svg width="10" height="11" viewBox="0 0 10 11"><path d="M0 0 L10 5.5 L0 11 L3 5.5 Z" fill="var(--leaf-green)"/></svg>Anxiety</li>
      <li><svg width="10" height="11" viewBox="0 0 10 11"><path d="M0 0 L10 5.5 L0 11 L3 5.5 Z" fill="var(--leaf-green)"/></svg>Depression</li>
      <li><svg width="10" height="11" viewBox="0 0 10 11"><path d="M0 0 L10 5.5 L0 11 L3 5.5 Z" fill="var(--leaf-green)"/></svg>Life Transitions</li>
      <li><svg width="10" height="11" viewBox="0 0 10 11"><path d="M0 0 L10 5.5 L0 11 L3 5.5 Z" fill="var(--leaf-green)"/></svg>Marriage Counseling</li>
      <li><svg width="10" height="11" viewBox="0 0 10 11"><path d="M0 0 L10 5.5 L0 11 L3 5.5 Z" fill="var(--leaf-green)"/></svg>Separation and Divorce</li>
      <li><svg width="10" height="11" viewBox="0 0 10 11"><path d="M0 0 L10 5.5 L0 11 L3 5.5 Z" fill="var(--leaf-green)"/></svg>Women’s Issues</li>
      <li><svg width="10" height="11" viewBox="0 0 10 11"><path d="M0 0 L10 5.5 L0 11 L3 5.5 Z" fill="var(--leaf-green)"/></svg>Addictions and Infidelity</li>
      <li><svg width="10" height="11" viewBox="0 0 10 11"><path d="M0 0 L10 5.5 L0 11 L3 5.5 Z" fill="var(--leaf-green)"/></svg>Parent/Child Relationships</li>
      <li><svg width="10" height="11" viewBox="0 0 10 11"><path d="M0 0 L10 5.5 L0 11 L3 5.5 Z" fill="var(--leaf-green)"/></svg>Family Conflict</li>
      <li><svg width="10" height="11" viewBox="0 0 10 11"><path d="M0 0 L10 5.5 L0 11 L3 5.5 Z" fill="var(--leaf-green)"/></svg>Trauma/Grief and Loss</li>
    </ul>
  </div>

  <div class="brand">
    <span class="brand-dot"></span>
    <span class="brand-name">Calm Harbor<br>Counseling</span>
  </div>

  <h2 class="cta">CALL TO SCHEDULE<span class="cta-highlight">A FREE 20 MINUTE</span>CONSULTATION</h2>

  <svg class="contact-band" viewBox="0 0 550 76" preserveAspectRatio="none">
    <path d="M0 14 Q275 -6 550 14 L550 76 L0 76 Z" fill="#111"/>
    <path d="M0 18 Q275 0 550 18 L550 76 L0 76 Z" fill="var(--band-green)"/>
  </svg>
  <div class="contact-text">
    <p class="contact-address">3840 W. 58th Street #2200 Tulsa, OK 74129</p>
    <p class="contact-lines">www.calmharborcare.example | dana@calmharborcare.example | (918) 555-0148</p>
    <p class="contact-promise">It is my desire for you to discover that no matter the situation you are currently going through….. there’s calm ahead!</p>
  </div>
</section>

</body>
</html>
```